Game, Voice & Dedicated Server Company Needs a Business Card Design

We need a new business card design, centered around our new logo (PSD provided below).

Designs that we do like:
https://pixelmarsh.net/item/corporate-business-card/5382017?s_rank=43 (needs to be made more eye catching)

Our main areas of business are:
- Dedicated Servers
- Game Servers
- Voice Servers
- Mitigation Security Specialists

Industry/Entity Type

Business

Contact Information for Business Card

On the card: (and anything else you would suggest)
- Staff member name
- Staff member position in company
- Staff member phone number
- Staff member email
- Other / Staff member Skype
- Website link

Colors
9bcb3c
abd036

Requirements
Must have
• Design of Card:
• - Green (same green as the logo)
• - Business / Corporate design
• - Something a little different / abstract that shouts premium

```html
<!DOCTYPE html>
<html lang="en">
<head>
<meta charset="utf-8">
<title>Brightwave Hosting – Business Card</title>
<link rel="stylesheet" href="https://fonts.googleapis.com/css2?family=Source+Sans+3:wght@400;600;700&display=swap">
<style>
  :root {
    --backdrop: #141414;
    --paper: #ffffff;
    --brand-green: #9fd23a;
    --ink: #1c1c1c;
    --on-green: #ffffff;
  }
  * { box-sizing: border-box; margin: 0; padding: 0; }
  html, body { width: 1200px; height: 900px; overflow: hidden; }
  body {
    background: var(--backdrop);
    font-family: "Source Sans 3", "Myriad Pro", sans-serif;
    position: relative;
  }
  .card {
    position: absolute;
    top: 170px;
    width: 347px;
    height: 561px;
  }
  .card--front { left: 259px; background: var(--paper); }
  .card--back { left: 631px; background: var(--brand-green); }

  .accent-band {
    position: absolute;
    left: 102px;
    width: 143px;
    height: 30px;
    background: var(--brand-green);
  }
  .accent-band--top { top: 0; }
  .accent-band--bottom { bottom: 0; height: 28px; }

  .brand-badge {
    position: absolute;
    top: 150px;
    left: 0;
    width: 100%;
    display: flex;
    justify-content: center;
    align-items: center;
    gap: 10px;
    font-weight: 700;
    font-size: 26px;
    color: var(--brand-green);
  }
  .brand-badge__square {
    width: 20px; height: 20px;
    background: var(--brand-green);
  }

  .contact {
    position: absolute;
    top: 271px;
    left: 0;
    width: 100%;
    text-align: center;
    color: var(--ink);
    font-size: 15px;
    line-height: 20px;
  }
  .contact__name {
    color: var(--brand-green);
    font-weight: 600;
    font-size: 19px;
    line-height: 24px;
  }
  .contact__role { margin-bottom: 26px; }
  .contact__group { margin-bottom: 18px; }

  .wordmark {
    position: absolute;
    top: 276px;
    left: 36px;
    color: var(--on-green);
    font-weight: 700;
    font-size: 40px;
    line-height: 38px;
    letter-spacing: -0.5px;
  }
  .wordmark__line--small { font-size: 33px; }

  .services {
    position: absolute;
    top: 431px;
    left: 100px;
    list-style: none;
    color: var(--on-green);
    font-size: 15.5px;
    line-height: 20.5px;
  }
  .services li::before {
    content: "•";
    margin-right: 6px;
  }
</style>
</head>
<body>
  <section class="card card--front">
    <div class="accent-band accent-band--top"></div>
    <div class="brand-badge">
      <span class="brand-badge__square"></span>
      <span>Brightwave</span>
    </div>
    <div class="contact">
      <p class="contact__name">Daniel Carter</p>
      <p class="contact__role">Managing Director</p>
      <div class="contact__group">
        <p>(044) 987 654 321</p>
        <p>hello@brightwavehost.net</p>
      </div>
      <div class="contact__group">
        <p>www.brightwavehost.net</p>
        <p>www.talkline.net</p>
      </div>
      <p>5678, Harbour Lane,Country, 54321</p>
    </div>
    <div class="accent-band accent-band--bottom"></div>
  </section>

  <section class="card card--back">
    <h1 class="wordmark">
      <span>BRIGHTWAVE</span><br>
      <span class="wordmark__line--small">HOSTING</span>
    </h1>
    <ul class="services">
      <li>Dedicated Servers</li>
      <li>Game Servers</li>
      <li>Voice Servers</li>
      <li>Business relations</li>
    </ul>
  </section>
</body>
</html>
```